Simple and clean

We need a business card design for a new company called Dwelling Owl. It is a search engine to find current properties for sale or rent in New Zealand market.
We have already a colour scheme that we would like people to use.
Light brown: #D4CCB0
Light green: #D6E4D4
Green: #669966
Black/White
It is OK to divert from this colour scheme slightly as long as there is a green component to the business card.
Final design should be clean, simple and should communicate the nature of the business.
Target Market(s)
- First home buyers
- Real estate agents
- People seeking rentals
Industry/Entity Type
Business
Requirements
Must have
- Use those or similar colours.
Light brown: #D4CCB0
Light green: #D6E4D4
Green: #669966
Black/White

```html
<!DOCTYPE html>
<html lang="en">
<head>
<meta charset="utf-8">
<title>Dwelling Owl – Business Card</title>
<link rel="stylesheet" href="https://fonts.googleapis.com/css2?family=Source+Sans+3:ital,wght@0,400;0,700;1,400&display=swap">
<style>
  :root {
    --sand: #d4d8b0;
    --mint: #d9f5d3;
    --white: #ffffff;
    --black: #000000;
    --brand-green: #5cbf46;
    --frame: #a8a8a8;
    --ring: #2b2b2b;
    --disc: #e6e6e6;
  }
  html, body {
    margin: 0;
    padding: 0;
    width: 1200px;
    height: 702px;
    overflow: hidden;
    background: var(--white);
  }
  .card {
    position: relative;
    width: 1200px;
    height: 702px;
    box-sizing: border-box;
    border: 3px solid var(--frame);
    background: var(--sand);
    overflow: hidden;
    font-family: "Source Sans 3", "Myriad Pro", sans-serif;
  }
  .card__shapes {
    position: absolute;
    inset: 0;
    width: 100%;
    height: 100%;
  }
  .swoosh { fill: var(--mint); }
  .panel  { fill: var(--white); }
  .base   { fill: var(--black); }
  .brand-disc { fill: var(--disc); stroke: var(--ring); stroke-width: 7; }

  .brand-name {
    position: absolute;
    left: 236px;
    top: 42px;
    margin: 0;
    font-size: 76px;
    font-weight: 400;
    line-height: 1;
    letter-spacing: -0.5px;
    color: var(--brand-green);
  }
  .contact {
    position: absolute;
    right: 66px;
    top: 210px;
    text-align: right;
    color: var(--black);
  }
  .contact__name {
    margin: 0;
    font-size: 36px;
    font-weight: 700;
    line-height: 1.1;
  }
  .contact__role {
    margin: 4px 0 0;
    font-size: 31px;
    font-style: italic;
    line-height: 1.1;
  }
  .contact__details {
    margin: 42px 0 0;
    font-size: 29px;
    line-height: 1.52;
  }
  .website {
    position: absolute;
    right: 66px;
    bottom: 50px;
    margin: 0;
    font-size: 52px;
    line-height: 1;
    color: var(--white);
  }
</style>
</head>
<body>
  <div class="card">
    <svg class="card__shapes" viewBox="0 0 1084 634" preserveAspectRatio="none" aria-hidden="true">
      <path class="swoosh" d="M 75 634 C 150 380, 430 160, 1084 128 L 1084 634 Z"/>
      <path class="panel" d="M 140 634 C 190 500, 240 400, 295 345 C 430 205, 700 135, 1084 132 L 1084 634 Z"/>
      <path class="base" d="M 140 634 C 190 500, 240 400, 295 345 C 450 440, 760 492, 1084 490 L 1084 634 Z"/>
      <circle class="brand-disc" cx="127" cy="107" r="72"/>
    </svg>

    <h1 class="brand-name">Dwelling Owl</h1>

    <div class="contact">
      <p class="contact__name">Liam Carter</p>
      <p class="contact__role">Director</p>
      <p class="contact__details">
        Mobile: 04x-xxx-xxxx<br>
        Email: l.carter@dwellingowl.co.nz
      </p>
    </div>

    <p class="website">www.dwellingowl.co.nz</p>
  </div>
</body>
</html>
```